BrivoMatex. Lantern for the Steady Growth. Business card

Professional business card for BrivoMatex (Lantern for the Steady Growth)
My rationale: Strategy-> Execution-> Results-> Value that lead to the BrivoMatex name: We put the Lantern for the Steady Growth.
We deliver value to our customers helping them at defining a good strategy (cyan arrow). 90% of well formulated strategies fail due to poor execution so we also consider strategical execution very important (green arrow). Due to the execution we obtain the results (blue arrow). Finally, the results provide feedback to redefine strategy, and the new strategy has to be executed and new results obtained providing new feedback and on and on. It's like a wheel that finally, must create corporate value: value for shareholders, staholders, employees, providers...-

Target Market(s)

CEOs and steering comitees , invewrnent funds

Industry/Entity Type

Business Consultant

Contact Information for Business Card

Tommaso Ferlini
CEO & Founder
tommaso.ferlini@brivomatex.example
Mobile: +34 611.205.938
www.brivomatex.example

Colors

Designer to choose colors to be used in the design.

Requirements
Nice to have
• Nice to hace the words: Strategy, execution, results
• Nice to vave the claim: Lantern for the Steady Growth
• The three colors should be shown:
• cyan for STRATEGY
• green for EXECUTION
• blue for RESULTS
Should not have
• Complete black background

```html
<!DOCTYPE html>
<html lang="en">
<head>
<meta charset="UTF-8">
<title>BrivoMatex – Business Card</title>
<link href="https://fonts.googleapis.com/css2?family=Montserrat:wght@500;600;700;800&display=swap" rel="stylesheet">
<style>
  :root {
    --brand-blue: #0b35a3;
    --brand-cyan: #16aeea;
    --ink: #1c2230;
    --paper: #ffffff;
    --backdrop: #e6e8ea;
  }
  * { box-sizing: border-box; margin: 0; padding: 0; }
  html, body { width: 1200px; height: 1000px; overflow: hidden; }
  body {
    background: var(--backdrop);
    font-family: "Montserrat", Arial, sans-serif;
    position: relative;
  }
  .card {
    position: absolute;
    left: 250px;
    width: 700px;
    height: 400px;
    border-radius: 30px;
    overflow: hidden;
    box-shadow: 0 10px 30px rgba(0,0,0,0.12);
  }
  /* Back side */
  .card-back {
    top: 60px;
    background: var(--brand-blue);
    color: var(--paper);
    display: flex;
    flex-direction: column;
    align-items: center;
    justify-content: center;
  }
  .card-back .brand-name {
    font-size: 54px;
    font-weight: 800;
    letter-spacing: -0.5px;
  }
  .card-back .brand-web {
    margin-top: 34px;
    font-size: 14px;
    font-weight: 500;
    letter-spacing: 3px;
  }
  /* Front side */
  .card-front {
    top: 520px;
    background: var(--paper);
  }
  .front-identity {
    position: absolute;
    left: 50px;
    top: 110px;
    color: var(--brand-blue);
  }
  .front-identity .brand-name {
    font-size: 56px;
    font-weight: 800;
    letter-spacing: -1px;
  }
  .person-name {
    margin-top: 18px;
    font-size: 25px;
    font-weight: 800;
  }
  .person-role {
    margin-top: 4px;
    font-size: 14px;
    font-weight: 600;
    letter-spacing: 1px;
    color: var(--ink);
  }
  .contact-list {
    position: absolute;
    left: 400px;
    top: 170px;
    list-style: none;
    font-size: 14px;
    font-weight: 500;
    color: var(--ink);
  }
  .contact-list li {
    display: flex;
    align-items: center;
    gap: 10px;
    margin-bottom: 10px;
  }
  .contact-list svg { width: 16px; height: 16px; flex: none; }
  .card-bands {
    position: absolute;
    left: 0; bottom: 0;
    width: 700px; height: 110px;
  }
  .tagline {
    position: absolute;
    right: 48px;
    bottom: 48px;
    font-size: 16px;
    font-weight: 600;
    color: var(--paper);
    letter-spacing: 0.5px;
  }
</style>
</head>
<body>

  <section class="card card-back" aria-label="Business card, back">
    <div class="brand-name">BrivoMatex</div>
    <div class="brand-web">www.brivomatex.example</div>
  </section>

  <section class="card card-front" aria-label="Business card, front">
    <div class="front-identity">
      <div class="brand-name">BrivoMatex</div>
      <div class="person-name">Tommaso Ferlini</div>
      <div class="person-role">CEO, FOUNDER</div>
    </div>

    <ul class="contact-list">
      <li>
        <svg viewBox="0 0 16 16" aria-hidden="true"><path fill="var(--brand-cyan)" d="M3.5 1.5l2.5 0 1 3.5-1.8 1.2a8 8 0 0 0 4.6 4.6L11 9l3.5 1v2.5c0 1-1 2-2 2A11 11 0 0 1 1.5 3.5c0-1 1-2 2-2z"/></svg>
        +34 611.205.938
      </li>
      <li>
        <svg viewBox="0 0 16 16" aria-hidden="true"><rect x="1" y="3" width="14" height="10" rx="1" fill="var(--brand-cyan)"/><path d="M1.5 3.8L8 9l6.5-5.2" stroke="#fff" stroke-width="1.4" fill="none"/></svg>
        tommaso.ferlini@brivomatex.example
      </li>
      <li>
        <svg viewBox="0 0 16 16" aria-hidden="true"><circle cx="8" cy="8" r="6.5" fill="none" stroke="var(--brand-cyan)" stroke-width="1.5"/><ellipse cx="8" cy="8" rx="2.8" ry="6.5" fill="none" stroke="var(--brand-cyan)" stroke-width="1.2"/><path d="M1.5 8h13" stroke="var(--brand-cyan)" stroke-width="1.2"/></svg>
        www.brivomatex.example
      </li>
    </ul>

    <svg class="card-bands" viewBox="0 0 700 110" aria-hidden="true">
      <rect x="0" y="96" width="700" height="14" fill="var(--brand-cyan)"/>
      <path d="M380 110 L400 55 Q410 30 440 30 L700 30 L700 110 Z" fill="var(--brand-blue)"/>
    </svg>
    <div class="tagline">Your Tagline Here</div>
  </section>

</body>
</html>
```